Infographic for council approvals process

Looking to show the different steps that a person needs to undertake to get local council approval for their new swimming pool. It's a bit convoluted and text heavy when written out, but could be more graphically illustrated as a series of steps and choices.
Needs to be aligned to the brand for www.LagoonBuildPacksOnline.com.au

Target Market(s)

Home Owners

Font styles to use
Sans Serif

Requirements
Must have
• Nice graphics that help simplify and layout the process graphically, the infographic should reference our brand colours and logos.

```html
<!DOCTYPE html>
<html lang="en">
<head>
<meta charset="utf-8">
<title>Lagoon Build Packs Online – Pool Approval Guide</title>
<link href="https://fonts.googleapis.com/css2?family=Montserrat:wght@400;500;600;700;800&display=swap" rel="stylesheet">
<style>
:root{
  --navy:#003b5c;
  --navy-deep:#062f4a;
  --teal:#6ccaca;
  --teal-light:#a8e1df;
  --teal-pale:#e3f5f4;
  --grey-bg:#6f747b;
  --ink:#4a5560;
  --white:#ffffff;
}
*{margin:0;padding:0;box-sizing:border-box}
html,body{width:1008px;height:1200px;overflow:hidden;background:var(--grey-bg);font-family:'Montserrat',sans-serif}
.canvas{position:relative;width:1008px;height:1200px}
.page{position:absolute;width:350px;height:494px;background:var(--white);overflow:hidden}
.abs{position:absolute}
.page svg.layer{position:absolute;left:0;top:0}

/* cover */
.cover{left:125px;top:81px}
.brand{left:0;width:350px;top:22px;height:30px;display:flex;justify-content:center;align-items:center;gap:8px;z-index:3}
.brand-dot{width:22px;height:22px;border-radius:50%;background:var(--teal);flex:none}
.brand-name{color:var(--navy);font-weight:700;font-size:11px;line-height:13px;letter-spacing:.4px;text-transform:uppercase}
.cover-headline{left:0;width:350px;top:290px;text-align:center;color:var(--white);font-weight:800;font-size:15.5px;line-height:20px;letter-spacing:.3px;z-index:2}
.cover-url{left:0;width:350px;top:354px;text-align:center;color:var(--white);font-weight:500;font-size:10.5px;z-index:2}
.badge{position:absolute;top:404px;width:62px;height:62px;z-index:2}
.badge-text{position:absolute;left:0;width:62px;text-align:center;color:var(--navy);font-weight:700}

/* approval page */
.approval{left:533px;top:81px}
.step-num{color:var(--white);font-weight:800;font-size:22px}
.hero-title{left:75px;top:43px;color:var(--white);font-weight:800;font-size:13.5px;line-height:18px;letter-spacing:.2px}
.intro{left:22px;width:310px;color:var(--ink);font-size:5.6px;line-height:9.5px}
.lead{left:22px;width:316px;color:var(--navy);font-weight:700;font-size:7.5px;line-height:10.5px}
.nsw-banner{left:17px;top:219px;width:300px;height:27px;background:var(--teal);border-radius:6px}
.nsw-title{left:10px;top:3px;color:var(--white);font-weight:800;font-size:12.5px}
.nsw-sub{left:11px;top:18px;color:var(--navy-deep);font-weight:700;font-size:4.6px}
.option-title{color:var(--navy);font-weight:800;font-size:10px}
.option-body{width:120px;color:var(--ink);font-size:5.6px;line-height:9.9px;text-align:justify}
.site-url{left:0;width:350px;text-align:center;color:var(--white);font-weight:600;font-size:7px}

/* document pages */
.docs{top:627px}
.docs-da{left:128px}
.docs-cdc{left:531px}
.num-block{left:0;top:0;width:60px;height:60px;background:var(--navy);display:flex;align-items:center;justify-content:center;color:var(--white);font-weight:700;font-size:33px}
.page-title{left:76px;top:12px;color:var(--navy);font-size:14.5px;line-height:18px;font-weight:500;letter-spacing:.3px}
.page-title b{font-weight:800}
.rule{left:60px;top:60px;width:290px;height:1px;background:var(--navy)}
.doc-label{position:absolute;color:var(--navy);font-weight:700;font-size:10px;line-height:11.3px;letter-spacing:.2px}
.doc-note{position:absolute;color:var(--ink);font-size:5.6px;line-height:9.9px}
.after-title{left:18px;top:314px;color:var(--white);font-weight:800;font-size:12.5px}
.after-text{position:absolute;color:#c9dbe6;font-size:5.6px;line-height:9.9px}
.footnote{left:17px;top:446px;width:320px;color:#c9dbe6;font-size:5.6px;line-height:9.9px}
</style>
</head>
<body>
<div class="canvas">

  <!-- COVER -->
  <section class="page cover">
    <div class="abs" role="img" aria-label="Photo of a backyard fibreglass pool with a pergola, outdoor chairs and garden" style="left:0;top:60px;width:350px;height:340px;background:linear-gradient(180deg,#3d3a36 0%,#5a554d 35%,#2f6fb8 60%,#1d5fb0 100%)"></div>
    <svg class="layer" width="350" height="494" viewBox="0 0 350 494" aria-hidden="true">
      <path d="M0,0 H350 V72 q-22,-10 -44,0 t-44,0 t-44,0 t-44,0 t-44,0 t-44,0 t-44,0 t-42,0 Z" fill="#fff"/>
      <path d="M0,494 V396 q22,-10 44,0 t44,0 t44,0 t44,0 t44,0 t44,0 t44,0 t42,0 V494 Z" fill="#fff"/>
      <g fill="none" stroke="#fff" stroke-width="1">
        <circle cx="175" cy="344" r="6"/><ellipse cx="175" cy="344" rx="2.6" ry="6"/><line x1="169" y1="344" x2="181" y2="344"/>
      </g>
    </svg>
    <div class="abs brand"><span class="brand-dot"></span><span class="brand-name">Lagoon Build<br>Packs Online</span></div>
    <div class="abs cover-headline">AFFORDABLE DIY FIBREGLASS<br>POOLS DIRECT TO YOUR DOOR</div>
    <div class="abs cover-url">www.LagoonBuildPacksOnline.com.au</div>

    <div class="badge" style="left:27px">
      <svg width="62" height="62" viewBox="0 0 62 62" aria-hidden="true"><circle cx="31" cy="31" r="29" fill="#fff" stroke="#6ccaca" stroke-width="3"/><path d="M4,34 H58 A27,27 0 0 1 4,34Z" fill="#6ccaca"/><path d="M26,48 l5,3 l5,-3" fill="none" stroke="#003b5c" stroke-width="1.4"/><path d="M26,12 l10,10 M36,12 l-10,10" stroke="#003b5c" stroke-width="2"/></svg>
      <div class="badge-text" style="top:25px;font-size:5px">DIY</div>
      <div class="badge-text" style="top:37px;font-size:4.5px">INSTALLATION</div>
    </div>
    <div class="badge" style="left:106px">
      <svg width="62" height="62" viewBox="0 0 62 62" aria-hidden="true"><circle cx="31" cy="31" r="29" fill="#fff" stroke="#6ccaca" stroke-width="3"/><path d="M4,34 H58 A27,27 0 0 1 4,34Z" fill="#6ccaca"/><path d="M26,48 l5,3 l5,-3" fill="none" stroke="#003b5c" stroke-width="1.4"/><rect x="23" y="14" width="11" height="8" fill="#003b5c"/><path d="M34,16 h4 l3,3 v3 h-7z" fill="#003b5c"/><circle cx="26" cy="23" r="1.6" fill="#003b5c"/><circle cx="37" cy="23" r="1.6" fill="#003b5c"/></svg>
      <div class="badge-text" style="top:27px;font-size:5px">DELIVERY</div>
      <div class="badge-text" style="top:38px;font-size:4.5px">INCLUDED</div>
    </div>
    <div class="badge" style="left:185px">
      <svg width="62" height="62" viewBox="0 0 62 62" aria-hidden="true"><circle cx="31" cy="31" r="29" fill="#fff" stroke="#6ccaca" stroke-width="3"/><path d="M4,34 H58 A27,27 0 0 1 4,34Z" fill="#6ccaca"/><path d="M26,48 l5,3 l5,-3" fill="none" stroke="#003b5c" stroke-width="1.4"/></svg>
      <div class="badge-text" style="top:10px;font-size:12px;font-weight:800">25</div>
      <div class="badge-text" style="top:25px;font-size:4.5px">YEAR</div>
      <div class="badge-text" style="top:38px;font-size:4.5px">WARRANTY</div>
    </div>
    <div class="badge" style="left:264px">
      <svg width="62" height="62" viewBox="0 0 62 62" aria-hidden="true"><circle cx="31" cy="31" r="29" fill="#fff" stroke="#6ccaca" stroke-width="3"/><path d="M26,46 l5,3 l5,-3" fill="none" stroke="#003b5c" stroke-width="1.4"/></svg>
      <div class="badge-text" style="top:18px;font-size:4.5px">SINCE</div>
      <div class="badge-text" style="top:24px;font-size:13px;font-weight:800">2013</div>
    </div>
  </section>

  <!-- 01 APPROVAL -->
  <section class="page approval">
    <div class="abs" role="img" aria-label="Photo of a resort-style pool at dusk with a poolside cabana and palm trees" style="left:0;top:0;width:350px;height:128px;background:linear-gradient(180deg,#2b2a28 0%,#4b3b2c 55%,#2f5f80 100%)"></div>
    <div class="abs" style="left:8px;top:113px;width:334px;height:40px;background:#fff;border-radius:8px 8px 0 0"></div>
    <div class="abs step-num" style="left:29px;top:44px">01</div>
    <div class="abs" style="left:61px;top:27px;width:1px;height:62px;background:#fff"></div>
    <div class="abs hero-title">WHAT DO I NEED TO DO<br>TO GET MY POOL APPROVED?</div>

    <p class="abs intro" style="top:125px">Navigating the planning requirements for installing a swimming pool can be a complex process, varying significantly across different Australian states</p>
    <p class="abs lead" style="top:151px">In New South Wales (NSW), Queensland (QLD), Victoria (VIC), and the Australian Capital Territory (ACT), understanding the specific regulations and procedures is crucial for a successful project.</p>
    <p class="abs intro" style="top:188px">Each state has its own approval process, required permits, compliance standards, and inspection procedures.</p>

    <div class="abs nsw-banner">
      <div class="abs nsw-title">Council Approval for a Pool in NSW</div>
      <div class="abs nsw-sub">In NSW, every new pool construction must receive approval from a Licensed Certifier.</div>
    </div>
    <svg class="layer" width="350" height="494" viewBox="0 0 350 494" aria-hidden="true">
      <circle cx="299" cy="232" r="29" fill="#fff" stroke="#6ccaca" stroke-width="4"/>
    </svg>
    <div class="abs" role="img" aria-label="Map outline of New South Wales" style="left:281px;top:218px;width:36px;height:28px;background:var(--navy);border-radius:4px"></div>

    <p class="abs lead" style="top:271px;left:18px">Depending on the specific circumstances, some pools may need a Complying Development (CDC), while others will need a Development Application (DA) approval from the council.</p>

    <div class="abs option-title" style="left:21px;top:323px">Option 1 : CDC</div>
    <p class="abs option-body" style="left:19px;top:339px">Most customers prefer to apply for a CDC as it is a faster, cheaper and straight forward process with a private certifier instead of the local council. In order to apply for a CDC, certain criteria need to be met. Make sure you look at this criteria to ensure you are eligible.</p>

    <svg class="layer" width="350" height="494" viewBox="0 0 350 494" aria-hidden="true">
      <line x1="175" y1="312" x2="175" y2="326" stroke="#003b5c" stroke-width="1"/>
      <path d="M175,326 A25,25 0 0 1 175,376 A25,25 0 0 0 175,426" fill="none" stroke="#003b5c" stroke-width="12"/>
      <line x1="175" y1="426" x2="175" y2="445" stroke="#003b5c" stroke-width="1"/>
      <circle cx="175" cy="354" r="15" fill="#6ccaca"/>
      <circle cx="175" cy="398" r="15" fill="#6ccaca"/>
      <text x="175" y="357" text-anchor="middle" font-family="Montserrat,sans-serif" font-weight="800" font-size="9" fill="#fff">CDC</text>
      <text x="175" y="401" text-anchor="middle" font-family="Montserrat,sans-serif" font-weight="800" font-size="9" fill="#fff">DA</text>
      <path d="M0,494 V466 q22,-12 44,0 t44,0 t44,0 t44,0 t44,0 t44,0 t44,0 t42,0 V494Z" fill="#003b5c"/>
      <rect x="0" y="470" width="350" height="24" fill="#003b5c"/>
      <g fill="none" stroke="#fff" stroke-width=".7"><circle cx="98" cy="481" r="3.6"/><ellipse cx="98" cy="481" rx="1.5" ry="3.6"/><line x1="94.4" y1="481" x2="101.6" y2="481"/></g>
    </svg>

    <div class="abs option-title" style="left:208px;top:325px">Option 2 : DA</div>
    <p class="abs option-body" style="left:207px;top:339px">If you don't meet the requirements for a CDC, you'll need to obtain development consent from your local Council by submitting a Development Application (DA). This is the sole approval pathway in certain scenarios, such as if you're building a new home. Unfortunately this is a longer and more expensive process so make sure you get this underway as soon as possible.</p>

    <div class="abs site-url" style="top:477px;left:6px">www.LagoonBuildPacksOnline.com.au</div>
  </section>

  <!-- 03 DA DOCUMENTS -->
  <section class="page docs docs-da">
    <div class="abs num-block">03</div>
    <div class="abs page-title">Documents for a<br><b>DA approval</b></div>
    <div class="abs rule"></div>

    <svg class="layer" width="350" height="494" viewBox="0 0 350 494" aria-hidden="true">
      <defs>
        <g id="da-ring">
          <circle r="18" fill="#e3f5f4" stroke="#6ccaca" stroke-width="3"/>
          <circle r="13" fill="#fff" stroke="#a8e1df" stroke-width="1"/>
          <rect x="-5" y="-7" width="10" height="13" rx="1" fill="none" stroke="#6ccaca" stroke-width="1"/>
          <line x1="-3" y1="-3" x2="3" y2="-3" stroke="#6ccaca" stroke-width=".8"/>
          <line x1="-3" y1="0" x2="3" y2="0" stroke="#6ccaca" stroke-width=".8"/>
          <line x1="-3" y1="3" x2="1" y2="3" stroke="#6ccaca" stroke-width=".8"/>
        </g>
      </defs>
      <use href="#da-ring" x="38" y="94"/>
      <use href="#da-ring" x="200" y="94"/>
      <use href="#da-ring" x="38" y="148"/>
      <use href="#da-ring" x="38" y="203"/>
      <use href="#da-ring" x="200" y="205"/>
      <use href="#da-ring" x="38" y="258"/>
      <use href="#da-ring" x="200" y="258"/>

      <path d="M0,494 V307 q22,-12 44,0 t44,0 t44,0 t44,0 t44,0 t44,0 t44,0 t42,0 V494Z" fill="#003b5c"/>
      <rect x="0" y="312" width="350" height="182" fill="#003b5c"/>
      <path d="M33,356 H313 l12,16 l-12,16 H33 l12,-16 Z" fill="#6ccaca"/>
      <path d="M116,356 l12,16 l-12,16 M210,356 l12,16 l-12,16" fill="none" stroke="#a8e1df" stroke-width="6"/>
      <g fill="#fff"><circle cx="80" cy="372" r="28"/><circle cx="174" cy="372" r="28"/><circle cx="268" cy="372" r="28"/></g>
      <g fill="none" stroke="#003b5c" stroke-width="1.3">
        <circle cx="83" cy="367" r="9"/><line x1="76" y1="374" x2="68" y2="382"/>
        <circle cx="174" cy="362" r="6"/><path d="M163,384 q11,-16 22,0"/><circle cx="181" cy="374" r="4"/>
        <rect x="258" y="360" width="20" height="18" rx="2"/><line x1="258" y1="365" x2="278" y2="365"/><path d="M264,372 l3,3 l6,-6"/><line x1="260" y1="380" x2="254" y2="386"/>
      </g>
    </svg>

    <div class="doc-label" style="left:68px;top:78px">Statement of<br>Environmental<br>Effect (SEE)</div>
    <div class="doc-label" style="left:228px;top:89px">Site Survey/Plan</div>
    <div class="doc-label" style="left:68px;top:128px">Detailed DA Design Drawings.</div>
    <p class="doc-note" style="left:68px;top:141px;width:260px">These should be completed by an architect or draftsperson and include a number of requirements, check with your local Council for what they require</p>
    <div class="doc-label" style="left:69px;top:186px">Structural Engineers<br>Pool Drawings and<br>Certification</div>
    <div class="doc-label" style="left:228px;top:193px">Builders Home<br>Warranty Insurance</div>
    <div class="doc-label" style="left:68px;top:240px">Copy of payment<br>receipt for Long<br>Service Levy</div>
    <div class="doc-label" style="left:228px;top:246px">Water Authority<br>Tap In Approval</div>

    <div class="abs after-title">What happens after my pool is installed?</div>
    <p class="after-text" style="left:42px;top:411px;width:75px;text-align:justify">When you're fibreglass pool and pool fence is installed, you'll be ready for a pool inspection. This is the last stage of the pool approval journey.</p>
    <p class="after-text" style="left:138px;top:410px;width:72px">An inspector will visit the site and ensure all regulations have been met.</p>
    <p class="after-text" style="left:223px;top:410px;width:97px;text-align:justify">The inspector will conduct inspections, measurements, tests, and capture photographs of your pool gates, pool fences, dividing fences utilised as pool fences, and any objects or structures in close proximity to the pool fence</p>
  </section>

  <!-- 02 CDC DOCUMENTS -->
  <section class="page docs docs-cdc">
    <div class="abs num-block">02</div>
    <div class="abs page-title" style="top:14px">What documents do<br><b>I need for a CDC?</b></div>
    <div class="abs rule"></div>

    <svg class="layer" width="350" height="494" viewBox="0 0 350 494" aria-hidden="true">
      <defs>
        <g id="cdc-ring">
          <circle r="18" fill="#e3f5f4" stroke="#6ccaca" stroke-width="3"/>
          <circle r="13" fill="#fff" stroke="#a8e1df" stroke-width="1"/>
          <rect x="-5" y="-7" width="10" height="13" rx="1" fill="none" stroke="#6ccaca" stroke-width="1"/>
          <line x1="-3" y1="-3" x2="3" y2="-3" stroke="#6ccaca" stroke-width=".8"/>
          <line x1="-3" y1="0" x2="3" y2="0" stroke="#6ccaca" stroke-width=".8"/>
          <path d="M-2,3 l1.5,1.5 l3,-3" fill="none" stroke="#6ccaca" stroke-width=".8"/>
        </g>
      </defs>
      <use href="#cdc-ring" x="38" y="107"/>
      <use href="#cdc-ring" x="38" y="167"/>
      <use href="#cdc-ring" x="38" y="229"/>
      <use href="#cdc-ring" x="197" y="229"/>
      <use href="#cdc-ring" x="38" y="288"/>
      <use href="#cdc-ring" x="197" y="288"/>
      <use href="#cdc-ring" x="38" y="344"/>
      <use href="#cdc-ring" x="197" y="344"/>
      <path d="M0,494 V408 q22,-12 44,0 t44,0 t44,0 t44,0 t44,0 t44,0 t44,0 t42,0 V494Z" fill="#003b5c"/>
      <rect x="0" y="412" width="350" height="82" fill="#003b5c"/>
    </svg>

    <div class="doc-label" style="left:68px;top:102px">CDC Application form</div>
    <div class="doc-label" style="left:67px;top:135px">Section 10.7 Certificate for the Site Address.</div>
    <p class="doc-note" style="left:68px;top:148px;width:250px">You can purchase this from your local Council and it will tell you if you are eligible for a CDC. This 10.7 Certificate will also notify you if your site is designated as a floodplain,heritage site,slope hazard zone, or acid sulphate soil risk area. This is important as you will need to consult with specific professionals for the approvals if any of these are identified.</p>
    <div class="doc-label" style="left:69px;top:217px">Deposited<br>Plan/88b.</div>
    <div class="doc-label" style="left:231px;top:223px">Title Search</div>
    <div class="doc-label" style="left:68px;top:271px">Architectural Plans<br>from an architect<br>or a draftsperson</div>
    <div class="doc-label" style="left:231px;top:273px">Local Water<br>Authority<br>Endorsement</div>
    <div class="doc-label" style="left:68px;top:333px">Pool Engineering<br>Drawings</div>
    <div class="doc-label" style="left:229px;top:327px">BASIX Certificate</div>
    <p class="doc-note" style="left:229px;top:339px;width:98px;text-align:justify">(Building Sustainability Index. This is only required if your pool is over 40,000L capacity)</p>

    <p class="abs footnote">Additional documents may be requested such as an arborist report,bushfire attack level or a flood certificate depending on your site</p>
  </section>

</div>
</body>
</html>
```